Social Media Cover and Profile

We already have our own logo. We just need a fresh design on our social media pages. We are not happy with our current designs. We would like to incorporate our YIKE billboard and the colors are blue (#05143f) and white. You can also incorporate silver as well. We are a family law office (Divorce and Custody) We no longer want to incorporate the Spire of Dunvale photo that we are currently using. You can look at our Facebook page; The Law Office of Miles T. Hadley.

Target Market(s)

Potential Clients

Industry/Entity Type

Family Law

Logo Text

Our Logo Is The Law Office of Miles T. Hadley with the Sheild

Requirements
Must have
• Text to include:
Central Pennslyvania's Premier Family Law Firm

Ability to be resized to and used as all images in social media, including but not limited to: Youtube Channel art, Facebook Cover and Profile.
Nice to have
• Darker color but we are open to "bright" ideas.

```html
<!DOCTYPE html>
<html lang="en">
<head>
<meta charset="utf-8">
<title>Miles T. Hadley – Social Cover Concepts</title>
<link href="https://fonts.googleapis.com/css2?family=Poppins:wght@300;400;600;800&display=swap" rel="stylesheet">
<style>
  :root {
    --board: #333333;
    --navy: #05143f;
    --white: #ffffff;
    --silver: #77717a;
    --grey-mark: #8c8c8c;
    --label: #ffffff;
  }
  * { margin: 0; padding: 0; box-sizing: border-box; }
  html, body { width: 848px; height: 1200px; overflow: hidden; background: var(--board); }
  body { position: relative; font-family: "Poppins", sans-serif; }

  .sample-label { position: absolute; left: 86px; width: 0; height: 0; color: var(--label); font-weight: 400; font-size: 15px; letter-spacing: 0.5px; }
  .sample-label span { position: absolute; white-space: nowrap; transform: translate(-50%, -50%) rotate(-90deg); }

  .cover { position: absolute; left: 130px; width: 642px; height: 243px; overflow: hidden; box-shadow: 0 4px 12px rgba(0,0,0,0.35); }
  .cover-1 { top: 73px; }
  .cover-2 { top: 348px; background: var(--navy); }
  .cover-3 { top: 624px; background: var(--white); }
  .cover-4 { top: 899px; background: var(--navy); }

  .photo { position: absolute; inset: 0; }
  .cover svg.shapes { position: absolute; inset: 0; width: 642px; height: 243px; }

  .photo-family {
    background:
      linear-gradient(90deg, #050505 0%, #0f0f0f 20%, rgba(20,18,16,0.75) 34%, rgba(20,18,16,0) 52%),
      radial-gradient(ellipse 16% 30% at 50% 52%, rgba(238,236,200,0.85), rgba(238,236,200,0) 100%),
      radial-gradient(ellipse 14% 26% at 80% 62%, rgba(240,230,222,0.85), rgba(240,230,222,0) 100%),
      radial-gradient(ellipse 12% 22% at 40% 62%, rgba(228,222,214,0.6), rgba(228,222,214,0) 100%),
      radial-gradient(ellipse 14% 40% at 96% 25%, rgba(178,226,205,0.9), rgba(178,226,205,0) 100%),
      linear-gradient(180deg, rgba(0,0,0,0) 70%, rgba(70,45,28,0.85) 100%),
      linear-gradient(90deg, #3a2a1e 30%, #9a6a3e 55%, #b27a46 72%, #c9cfbf 90%, #b7e0cc 100%);
  }
  .photo-desk {
    background:
      radial-gradient(ellipse 30% 45% at 38% 40%, rgba(232,160,70,0.85), rgba(232,160,70,0) 100%),
      radial-gradient(ellipse 16% 28% at 63% 72%, rgba(240,240,238,0.9), rgba(240,240,238,0) 100%),
      radial-gradient(ellipse 14% 22% at 55% 68%, rgba(214,170,140,0.8), rgba(214,170,140,0) 100%),
      radial-gradient(ellipse 26% 30% at 25% 78%, rgba(190,190,195,0.8), rgba(190,190,195,0) 100%),
      linear-gradient(180deg, rgba(0,0,0,0) 75%, rgba(40,30,22,0.7) 100%),
      linear-gradient(100deg, #7a7068 0%, #a08868 30%, #55575f 55%, #3a3d47 75%, #2e3038 100%);
  }
  .photo-handshake {
    background:
      linear-gradient(90deg, #141416 0%, rgba(20,20,22,0.8) 18%, rgba(20,20,22,0) 40%),
      radial-gradient(ellipse 20% 26% at 60% 40%, rgba(205,150,118,0.95), rgba(205,150,118,0) 100%),
      radial-gradient(ellipse 22% 24% at 88% 45%, rgba(232,236,240,0.9), rgba(232,236,240,0) 100%),
      radial-gradient(ellipse 16% 30% at 82% 72%, rgba(214,184,110,0.8), rgba(214,184,110,0) 100%),
      radial-gradient(ellipse 24% 30% at 40% 40%, rgba(50,52,60,0.9), rgba(50,52,60,0) 100%),
      linear-gradient(180deg, #9c9a9c 0%, #6e6a68 60%, #b8a884 100%);
  }

  .firm-name { position: absolute; left: 27px; display: flex; align-items: center; gap: 6px; font-weight: 400; text-transform: uppercase; line-height: 1; }
  .firm-name .mark { width: 29px; height: 33px; border: 1.5px solid currentColor; flex: none; }
  .firm-name .small { display: block; font-size: 5.5px; letter-spacing: 0.5px; margin-bottom: 2px; }
  .firm-name .big { display: block; font-size: 11px; letter-spacing: 0.6px; }

  .tagline { position: absolute; left: 27px; line-height: 1; }
  .tagline .region { display: block; font-weight: 400; font-size: 17px; letter-spacing: 0.1px; margin-bottom: 3px; }
  .tagline .lead { display: block; font-weight: 800; font-size: 25.5px; line-height: 25px; }

  .billboard { position: absolute; left: 27px; font-weight: 600; font-size: 42px; letter-spacing: 1px; line-height: 1; }

  .on-dark { color: var(--white); }
  .on-light { color: var(--navy); }
  .billboard.on-light { color: var(--grey-mark); }
</style>
</head>
<body>

  <div class="sample-label" style="top:194px"><span>SAMPLE 1</span></div>
  <div class="sample-label" style="top:469px"><span>SAMPLE 2</span></div>
  <div class="sample-label" style="top:745px"><span>SAMPLE 3</span></div>
  <div class="sample-label" style="top:1021px"><span>SAMPLE 4</span></div>

  <section class="cover cover-1">
    <div class="photo photo-family" role="img" aria-label="Photo of a young family with two children sitting at a kitchen table with paperwork"></div>
    <div class="firm-name on-dark" style="top:19px"><span class="mark"></span><span><span class="small">The Law Office of</span><span class="big">Miles T. Hadley</span></span></div>
    <div class="tagline on-dark" style="top:78px">
      <span class="region">CENTRAL PENNSLYVANIA'S</span>
      <span class="lead">PREMIER FAMILY</span>
      <span class="lead">LAW FIRM</span>
    </div>
    <div class="billboard on-dark" style="top:174px">YIKE</div>
  </section>

  <section class="cover cover-2">
    <div class="photo photo-desk" role="img" aria-label="Photo of a lawyer in a pinstripe suit writing notes beside a laptop"></div>
    <svg class="shapes" viewBox="0 0 642 243" aria-hidden="true">
      <path d="M0 0 H642 V93 C615 45 580 22 530 22 C450 22 360 85 250 128 C170 156 80 152 0 125 Z" fill="var(--navy)"/>
      <path d="M0 0 H642 V85 C615 37 580 14 530 14 C450 14 360 77 250 120 C170 148 80 144 0 117 Z" fill="var(--white)"/>
      <path d="M0 0 H642 V78 C615 28 580 6 530 6 C450 6 360 70 250 112 C170 140 80 135 0 108 Z" fill="var(--silver)"/>
      <path d="M0 0 H642 V72 C615 24 585 10 540 10 C450 10 360 62 250 104 C170 132 80 125 0 98 Z" fill="var(--navy)"/>
    </svg>
    <div class="tagline on-dark" style="top:29px">
      <span class="region">CENTRAL PENNSLYVANIA'S</span>
      <span class="lead">PREMIER FAMILY</span>
      <span class="lead">LAW FIRM</span>
    </div>
    <div class="billboard on-dark" style="top:175px">YIKE</div>
  </section>

  <section class="cover cover-3">
    <svg class="shapes" viewBox="0 0 642 243">
      <defs>
        <linearGradient id="panel-mother" x1="0" y1="0" x2="1" y2="1"><stop offset="0" stop-color="#c8c2bc"/><stop offset="0.5" stop-color="#6a6c70"/><stop offset="1" stop-color="#3a3c42"/></linearGradient>
        <linearGradient id="panel-meeting" x1="0" y1="0" x2="1" y2="1"><stop offset="0" stop-color="#b8a8a0"/><stop offset="0.5" stop-color="#5a5e66"/><stop offset="1" stop-color="#26282e"/></linearGradient>
        <linearGradient id="panel-gavel" x1="0" y1="0" x2="1" y2="1"><stop offset="0" stop-color="#2e2a28"/><stop offset="0.5" stop-color="#b08c72"/><stop offset="1" stop-color="#c8b070"/></linearGradient>
        <radialGradient id="panel-family" cx="0.5" cy="0.55" r="0.7"><stop offset="0" stop-color="#ece8c8"/><stop offset="0.4" stop-color="#b2825a"/><stop offset="0.85" stop-color="#8e6440"/><stop offset="1" stop-color="#b8dccb"/></radialGradient>
      </defs>
      <polygon role="img" aria-label="Photo of a mother comforting her daughter in a law office" points="273,0 399,0 380,77 254,77" fill="url(#panel-mother)"/>
      <polygon role="img" aria-label="Photo of a family meeting with a lawyer at a desk" points="249,84 378,84 359,160 230,160" fill="url(#panel-meeting)"/>
      <polygon role="img" aria-label="Photo of a handshake over a desk with a gavel and scales" points="226,166 358,166 339,243 207,243" fill="url(#panel-gavel)"/>
      <polygon role="img" aria-label="Photo of a young family with two children at a kitchen table" points="404,0 642,0 642,243 344,243" fill="url(#panel-family)"/>
    </svg>
    <div class="firm-name on-light" style="top:19px"><span class="mark"></span><span><span class="small">The Law Office of</span><span class="big">Miles T. Hadley</span></span></div>
    <div class="tagline on-light" style="top:78px">
      <span class="region">CENTRAL PENNSLYVANIA'S</span>
      <span class="lead">PREMIER FAMILY</span>
      <span class="lead">LAW FIRM</span>
    </div>
    <div class="billboard on-light" style="top:174px">YIKE</div>
  </section>

  <section class="cover cover-4">
    <div class="photo photo-handshake" role="img" aria-label="Photo of a business handshake above a desk with scales of justice"></div>
    <svg class="shapes" viewBox="0 0 642 243" aria-hidden="true">
      <path d="M0 84 C80 66 190 80 320 145 C420 195 500 232 560 230 C600 228 625 212 642 190 V243 H0 Z" fill="var(--silver)"/>
      <path d="M0 106 C80 86 190 96 310 150 C420 198 500 220 560 218 C600 216 625 200 642 160 V243 H0 Z" fill="var(--white)"/>
      <path d="M0 114 C80 94 190 104 310 158 C420 206 500 226 560 224 C600 222 625 206 642 168 V243 H0 Z" fill="var(--navy)"/>
    </svg>
    <div class="billboard on-dark" style="top:22px">YIKE</div>
    <div class="tagline on-dark" style="top:160px">
      <span class="region">CENTRAL PENNSLYVANIA'S</span>
      <span class="lead">PREMIER FAMILY</span>
      <span class="lead">LAW FIRM</span>
    </div>
  </section>

</body>
</html>
```